依頼概要
■依頼の目的/概要
大型施設の共有スペースに展示する商品のPOPのデザインをお願いします。
展示の全体イメージがありますのでそれに合わせたイメージで制作して下さい。

■依頼詳細
大型SC内の新店舗の商品展示用のPOPになります。
展示イメージに合うようにPOPの制作をして下さい。
前回の展示のPOPを参考にアップしておきますが、同じような配置にする必要はございません。
前回は背景色などは変えずに、商品名、金額等を、レディース、メンズ、キッズの三種類に色分けして区別しておりました。
今回はキッズはないのですが、レディース、メンズ、雑貨と別れておりますので、うまく区別できるような工夫をお願いします。
サイズは A4縦サイズ。
店舗によって商品、金額、アイテム数は変化するので、変更できるような仕様にして下さい。
フォントはモリサワでしたら入っております。
採用後は使用フォントを納品データと共にお知らせください。

■重視する点
Illustrator・Photoshopの経験必須でお願いします。
新店舗のPOPになりますので、」お客様の目に留まるようなデザインが望ましいです。

■継続依頼について
弊社ではこういった案件が多くあり、次回は母の日、父の日等もありますので、継続的依頼できるありがたいです。

その他何かご不明な点がございましたら、お気軽にご質問下さい。
よろしくお願いいたします。
参考用イメージをアップします。

今回の展示イメージ
前回のPOPイメージ

の2点です。
1店舗の最大アイテム数は6になります。
前回のPOP参考例はあくまで参考です。
同じように作作らなくても良いので参考程度にして頂ければ幸いです。
展示イメージにある通り、POPは各マネキン、雑貨の前に置くものになります。
新店舗のオープンなのでワクワクするようなイメージで制作してもらえればと思います。
集まりが少ないので当選額を上乗せします。
それに伴い期間も延長いたします。
ご応募いただきありがとうございました。

見やすくイメージに沿っていたため。

たくさんのご参加ありがとうございました。
ぜひ次回もご参加下さい。

```html
<!DOCTYPE html>
<html lang="ja">
<head>
<meta charset="utf-8">
<title>New Open POP</title>
<link rel="stylesheet" href="https://fonts.googleapis.com/css2?family=M+PLUS+Rounded+1c:wght@500;700;800;900&display=swap">
<style>
  :root {
    --red: #e8383d;
    --pink: #ef8fa3;
    --pink-strong: #f07f95;
    --pink-soft: #fbd6de;
    --price: #d8334a;
    --ink: #333333;
    --orange: #ef5a3f;
    --frame: #9a9a9a;
    --white: #ffffff;
  }
  * { margin: 0; padding: 0; box-sizing: border-box; }
  html, body { width: 849px; height: 1200px; overflow: hidden; background: var(--white); }
  body { font-family: "M PLUS Rounded 1c", sans-serif; color: var(--ink); }
  .pop { position: relative; width: 849px; height: 1200px; overflow: hidden; background: var(--white); }

  .glow { position: absolute; border-radius: 50%; }
  .glow-right { width: 260px; height: 260px; right: -80px; top: -30px;
    background: radial-gradient(circle, rgba(239,120,140,.75) 0%, rgba(239,143,163,.35) 55%, rgba(255,255,255,0) 72%); }
  .glow-left { width: 180px; height: 180px; left: -70px; top: -70px;
    background: radial-gradient(circle, rgba(239,143,163,.45) 0%, rgba(255,255,255,0) 70%); }

  .new-open { position: absolute; left: 22px; top: 30px; color: var(--red);
    font-weight: 900; font-size: 62px; line-height: 1; letter-spacing: 1px; }
  .title { position: absolute; left: 268px; top: 18px; color: var(--pink);
    font-weight: 800; font-size: 112px; line-height: 1.2; letter-spacing: 0;
    white-space: nowrap;
    -webkit-text-stroke: 4px var(--white); paint-order: stroke fill; }
  .comment { position: absolute; left: 16px; top: 178px; color: var(--pink-strong);
    font-weight: 800; font-size: 54px; line-height: 1.2; letter-spacing: 0; white-space: nowrap; }

  .illustration { position: absolute; left: 40px; top: 285px; width: 400px; height: 790px; }
  .grass { position: absolute; left: 230px; top: 910px; width: 619px; height: 170px; }

  .item { position: absolute; right: 0; }
  .item-band { height: 36px; padding-left: 16px; color: var(--white);
    font-weight: 700; font-size: 26px; line-height: 36px; white-space: nowrap;
    background: linear-gradient(90deg, var(--pink-strong) 0%, var(--pink) 45%, var(--pink-soft) 100%); }
  .item-price { color: var(--price); font-weight: 800; font-size: 46px; line-height: 1.05; padding-left: 62px; white-space: nowrap; }
  .item-tax { color: var(--price); font-weight: 700; font-size: 22px; padding-left: 118px; white-space: nowrap; }
  .item.col-a { left: 355px; }
  .item.col-b { left: 525px; }
  .item.col-b .item-price { padding-left: 90px; }
  .item.col-b .item-tax { padding-left: 146px; }

  .floor { position: absolute; left: -8px; top: 935px; width: 176px; height: 176px; border-radius: 50%;
    background: var(--orange); color: var(--white); font-weight: 900; font-size: 64px;
    display: flex; align-items: flex-start; justify-content: center; padding-top: 34px; }
  .footer { position: absolute; left: 0; top: 1060px; width: 849px; height: 140px; background: var(--white); }
  .shop-logo { position: absolute; left: 36px; top: 52px; font-size: 28px; font-weight: 700; white-space: nowrap; }
  .shop-name { position: absolute; left: 252px; top: 6px; width: 570px; height: 84px;
    border: 3px solid var(--frame); border-radius: 14px; padding: 18px 18px; font-size: 32px; font-weight: 700; }
  .corporate-logo { position: absolute; right: 30px; top: 96px; font-size: 20px; font-weight: 700; white-space: nowrap; }
</style>
</head>
<body>
<main class="pop">
  <div class="glow glow-right"></div>
  <div class="glow glow-left"></div>

  <div class="new-open">NEW<br>OPEN</div>
  <h1 class="title">タイトル</h1>
  <p class="comment">ーコメント●●●●●●●ー</p>

  <svg class="illustration" role="img" aria-label="Illustration of a deer with branching antlers and small leaves" viewBox="0 0 400 790" preserveAspectRatio="none">
    <defs>
      <radialGradient id="deerTone" cx="45%" cy="55%" r="60%">
        <stop offset="0%" stop-color="#8a5a3c" stop-opacity="0.55"/>
        <stop offset="100%" stop-color="#b99a7a" stop-opacity="0.15"/>
      </radialGradient>
    </defs>
    <rect width="400" height="790" rx="30" fill="url(#deerTone)"/>
  </svg>

  <svg class="grass" role="img" aria-label="Illustration of green grass" viewBox="0 0 619 170" preserveAspectRatio="none">
    <defs>
      <linearGradient id="grassTone" x1="0" y1="0" x2="0" y2="1">
        <stop offset="0%" stop-color="#dcefb8" stop-opacity="0"/>
        <stop offset="60%" stop-color="#9ccc52" stop-opacity="0.7"/>
        <stop offset="100%" stop-color="#9ccc52"/>
      </linearGradient>
    </defs>
    <rect width="619" height="170" fill="url(#grassTone)"/>
  </svg>

  <section class="items">
    <div class="item col-a" style="top:278px"><div class="item-band">アイテム</div><div class="item-price">3,000yen</div><div class="item-tax">(税込 3,080)</div></div>
    <div class="item col-b" style="top:410px"><div class="item-band">アイテム</div><div class="item-price">3,000yen</div><div class="item-tax">(税込 3,080)</div></div>
    <div class="item col-a" style="top:548px"><div class="item-band">アイテム</div><div class="item-price">3,000yen</div><div class="item-tax">(税込 3,080)</div></div>
    <div class="item col-b" style="top:676px"><div class="item-band">アイテム</div><div class="item-price">3,000yen</div><div class="item-tax">(税込 3,080)</div></div>
    <div class="item col-a" style="top:812px"><div class="item-band">アイテム</div><div class="item-price">3,000yen</div><div class="item-tax">(税込 3,080)</div></div>
    <div class="item col-b" style="top:940px"><div class="item-band">アイテム</div><div class="item-price">3,000yen</div><div class="item-tax">(税込 3,080)</div></div>
  </section>

  <div class="floor">2F</div>
  <footer class="footer">
    <span class="shop-logo">店舗ロゴ</span>
    <div class="shop-name">店舗名</div>
    <span class="corporate-logo">コーポレートロゴ</span>
  </footer>
</main>
</body>
</html>
```